Business Card Design Project

I have attached the logo and the colour pallete for the branding for the company.

Creative designs for business cards are needed.

The Company is modern corporate.

Industry/Entity Type

Business

```html
<!DOCTYPE html>
<html lang="en">
<head>
<meta charset="utf-8">
<title>Stepwise Business Cards</title>
<link rel="stylesheet" href="https://fonts.googleapis.com/css2?family=Poppins:wght@400;500&display=swap">
<style>
  :root {
    --canvas-bg: #e4e4e4;
    --card-white: #ffffff;
    --orange-light: #f58a35;
    --orange-deep: #ea5a2d;
    --band-dark: #7e2846;
    --band-light: #c8405e;
    --blush: #fbdcd1;
    --ink: #3b3636;
    --label: #8a3a2e;
    --icon-line: #ffffff;
  }
  * { box-sizing: border-box; margin: 0; padding: 0; }
  html, body { width: 1200px; height: 1000px; overflow: hidden; }
  body {
    background: var(--canvas-bg);
    font-family: "Poppins", sans-serif;
    position: relative;
  }
  .card {
    position: absolute;
    top: 350px;
    width: 520px;
    height: 300px;
    overflow: hidden;
    box-shadow: 0 10px 24px rgba(0,0,0,0.18);
  }
  .card-front { left: 50px; background: var(--card-white); }
  .card-back {
    left: 630px;
    background: linear-gradient(100deg, var(--orange-deep) 0%, var(--orange-light) 45%, var(--orange-deep) 100%);
  }
  .brand-name {
    font-family: "Poppins", sans-serif;
    font-weight: 500;
    color: var(--ink);
    letter-spacing: -1px;
    line-height: 1;
  }
  .front-header {
    height: 150px;
    display: flex;
    align-items: center;
    justify-content: center;
  }
  .front-header .brand-name { font-size: 52px; }
  .accent-band {
    height: 12px;
    background: linear-gradient(90deg, var(--band-dark), var(--band-light));
  }
  .contact-strip {
    height: 138px;
    background: linear-gradient(100deg, var(--orange-deep) 0%, var(--orange-light) 50%, var(--orange-deep) 100%);
    display: flex;
    justify-content: space-around;
    align-items: flex-start;
    padding: 20px 24px 0;
  }
  .contact-item {
    display: flex;
    flex-direction: column;
    align-items: center;
    gap: 10px;
  }
  .contact-icon { width: 34px; height: 34px; }
  .contact-label {
    font-size: 17px;
    color: var(--label);
    font-weight: 400;
  }
  .brand-panel {
    position: absolute;
    left: 0;
    top: 78px;
    width: 415px;
    height: 100px;
    background: var(--blush);
    display: flex;
    align-items: center;
    justify-content: center;
  }
  .brand-panel .brand-name { font-size: 52px; }
  .web-address {
    position: absolute;
    right: 22px;
    bottom: 40px;
    font-size: 21px;
    letter-spacing: 9px;
    color: var(--ink);
    font-weight: 400;
  }
</style>
</head>
<body>
  <section class="card card-front" aria-label="Business card front">
    <header class="front-header">
      <span class="brand-name">stepwise</span>
    </header>
    <div class="accent-band"></div>
    <div class="contact-strip">
      <div class="contact-item">
        <svg class="contact-icon" viewBox="0 0 34 34" fill="none" stroke="var(--icon-line)" stroke-width="2">
          <path d="M17 5c-5 0-8 3.6-8 8 0 6 8 14 8 14s8-8 8-14c0-4.4-3-8-8-8z"/>
          <circle cx="17" cy="13" r="3"/>
          <ellipse cx="17" cy="29" rx="7" ry="2"/>
        </svg>
        <span class="contact-label">Adresse</span>
      </div>
      <div class="contact-item">
        <svg class="contact-icon" viewBox="0 0 34 34" fill="none" stroke="var(--icon-line)" stroke-width="2">
          <circle cx="17" cy="17" r="14"/>
          <path d="M13 10c-2 2-2 5 0 9s5 6 8 6l2-2-3-3-2 1c-1.5-1-3-3-3.5-4.5l1-2-2.5-3z"/>
        </svg>
        <span class="contact-label">Telephone</span>
      </div>
      <div class="contact-item">
        <svg class="contact-icon" viewBox="0 0 34 34" fill="none" stroke="var(--icon-line)" stroke-width="2">
          <circle cx="17" cy="17" r="14"/>
          <circle cx="17" cy="17" r="4"/>
          <path d="M21 13v5c0 2 3 2 3-1a7 7 0 1 0-3 6"/>
        </svg>
        <span class="contact-label">E-mail</span>
      </div>
    </div>
  </section>

  <section class="card card-back" aria-label="Business card back">
    <div class="brand-panel">
      <span class="brand-name">stepwise</span>
    </div>
    <p class="web-address">www.stepwiseco.com</p>
  </section>
</body>
</html>
```